QV - menu design

Hi,

We require elegant menu design for upscale restaurant. Please find attached the logo and the menu items for your reference.

for inspiration, this is a good website: -
http://www.platewhisper.example/bellfoldnotes/about.php

We are very much open for Menu Size suggestions.

unfortunately the place is going under renovation, we don't have updated images to it. the closest look and feel to our place is http://varnelo.example ..

we are also open for creative options on the shape, the styles, etc. as long as it represents the fine dine feel ...

Thanks ...

Dear All,

We wouldlike to extend our apology for not being able to provide feedbacks on everysingle design. We were extremely busy and we have multiple contests opensimultaneously which makes the process even harder.

However,we would like to thank you all for the efforts you have put into designingour menu. It is very much appreciated …

We wishyou all success in your design ventures and we are quite positive that we willbe working with many of you on many projects in the soon future. 

Thanks & Regards,

TLG Team...

 

 

 

Industry/Entity Type

Restaurant

Requirements
Must have
• Please ensure that there are 'some' images in the menu ... this is very important.
Should not have
• IMPORTANT: -

1. Please DO NOT insert any currency sign to the menu
2. Please keep the prices of the menu at the end of the menu items descriptions NOT beside the menu item names. The font of the price should be similar to the menu item description and please DO NOT bold the numbers. the prices should be subtle.

Thank you ...

```html
<!DOCTYPE html>
<html lang="en">
<head>
<meta charset="utf-8">
<title>Quayview Café – The Breakfast</title>
<link rel="stylesheet" href="https://fonts.googleapis.com/css2?family=Montserrat:wght@400;600;700&family=Questrial&display=swap">
<style>
  :root {
    --paper: #d4dee7;
    --paper-light: #dde6ee;
    --paper-dark: #c6d2dc;
    --ink: #111418;
    --text: #1e2226;
    --logo: #3a3d40;
    --card-fill: rgba(255, 255, 255, 0.12);
  }
  * { box-sizing: border-box; margin: 0; padding: 0; }
  html, body { width: 1200px; height: 848px; overflow: hidden; }
  body {
    position: relative;
    background:
      radial-gradient(ellipse at 20% 30%, var(--paper-light) 0%, transparent 60%),
      radial-gradient(ellipse at 80% 75%, var(--paper-dark) 0%, transparent 65%),
      var(--paper);
    color: var(--text);
  }
  .brand {
    position: absolute;
    left: 114px;
    top: 44px;
    width: 172px;
    text-align: center;
    font-family: "Montserrat", sans-serif;
    font-weight: 400;
    font-size: 21px;
    letter-spacing: 3px;
    line-height: 1.25;
    color: var(--logo);
  }
  .section-tag {
    position: absolute;
    left: 972px;
    top: 44px;
    width: 184px;
    height: 48px;
    border: 3.6px solid var(--ink);
    display: flex;
    align-items: center;
    justify-content: center;
    font-family: "Montserrat", sans-serif;
    font-weight: 700;
    font-size: 17px;
    letter-spacing: 0.6px;
    color: var(--ink);
  }
  .menu-grid {
    position: absolute;
    left: 115px;
    top: 121px;
    display: grid;
    grid-template-columns: repeat(3, 327px);
    grid-auto-rows: 146px;
    column-gap: 30px;
    row-gap: 33px;
  }
  .dish {
    position: relative;
    border: 3.6px solid var(--ink);
    background: var(--card-fill);
  }
  .dish-photo {
    position: absolute;
    left: 10px;
    top: 9px;
    width: 120px;
    height: 120px;
    border-radius: 50%;
  }
  .photo-arabic {
    background: radial-gradient(circle at 40% 45%, #d9a24a 0%, #a8683a 45%, #6b4630 75%, #e8dccb 100%);
  }
  .photo-shawarma {
    background: radial-gradient(circle at 55% 40%, #f2e9d8 0%, #9bbd5a 35%, #c9995e 65%, #7e4e34 100%);
  }
  .photo-seafood {
    background: radial-gradient(circle at 50% 45%, #3a2e2a 0%, #c2562a 45%, #e0682c 75%, #d2471f 100%);
  }
  .dish-info {
    position: absolute;
    left: 146px;
    top: 27px;
    width: 172px;
  }
  .dish-name {
    font-family: "Montserrat", sans-serif;
    font-weight: 600;
    font-size: 11.5px;
    letter-spacing: 0.2px;
    color: var(--ink);
    margin-bottom: 13px;
  }
  .dish-desc {
    font-family: "Questrial", sans-serif;
    font-size: 9.2px;
    line-height: 12.6px;
    color: var(--text);
  }
</style>
</head>
<body>
  <header>
    <div class="brand">QUAYVIEW CAFÉ</div>
    <h1 class="section-tag">THE BREAKFAST</h1>
  </header>

  <main class="menu-grid">
    <article class="dish">
      <div class="dish-photo photo-arabic" role="img" aria-label="Photo of the Arabic breakfast platter"></div>
      <div class="dish-info">
        <h2 class="dish-name">THE ARABIC BREAKFAST</h2>
        <p class="dish-desc">One choice of hot beverage from our cafe served with our selection of scones, Smoked salmon and avocado sandwich, roasted sausages sandwich, grilled vegetables sandwich, of our best biscuits. 59</p>
      </div>
    </article>
    <article class="dish">
      <div class="dish-photo photo-shawarma" role="img" aria-label="Photo of chicken shawarma wraps"></div>
      <div class="dish-info">
        <h2 class="dish-name">CHICKEN SHAWARMA</h2>
        <p class="dish-desc">Served in the inimitable Quayview style with garlic sauce, cucumber and tomato pickles and three peppers coulis. 75</p>
      </div>
    </article>
    <article class="dish">
      <div class="dish-photo photo-seafood" role="img" aria-label="Photo of frutti di mare with mussels"></div>
      <div class="dish-info">
        <h2 class="dish-name">FRUTTI DI MARE</h2>
        <p class="dish-desc">Fresh cherry tomatoes, Mussels, Prawns, Calamari, Mozzarella, Olives. 99</p>
      </div>
    </article>

    <article class="dish">
      <div class="dish-photo photo-arabic" role="img" aria-label="Photo of the Arabic breakfast platter"></div>
      <div class="dish-info">
        <h2 class="dish-name">THE ARABIC BREAKFAST</h2>
        <p class="dish-desc">One choice of hot beverage from our cafe served with our selection of scones, Smoked salmon and avocado sandwich, roasted sausages sandwich, grilled vegetables sandwich, of our best biscuits. 59</p>
      </div>
    </article>
    <article class="dish">
      <div class="dish-photo photo-shawarma" role="img" aria-label="Photo of chicken shawarma wraps"></div>
      <div class="dish-info">
        <h2 class="dish-name">CHICKEN SHAWARMA</h2>
        <p class="dish-desc">Served in the inimitable Quayview style with garlic sauce, cucumber and tomato pickles and three peppers coulis. 75</p>
      </div>
    </article>
    <article class="dish">
      <div class="dish-photo photo-seafood" role="img" aria-label="Photo of frutti di mare with mussels"></div>
      <div class="dish-info">
        <h2 class="dish-name">FRUTTI DI MARE</h2>
        <p class="dish-desc">Fresh cherry tomatoes, Mussels, Prawns, Calamari, Mozzarella, Olives. 99</p>
      </div>
    </article>

    <article class="dish">
      <div class="dish-photo photo-arabic" role="img" aria-label="Photo of the Arabic breakfast platter"></div>
      <div class="dish-info">
        <h2 class="dish-name">THE ARABIC BREAKFAST</h2>
        <p class="dish-desc">One choice of hot beverage from our cafe served with our selection of scones, Smoked salmon and avocado sandwich, roasted sausages sandwich, grilled vegetables sandwich, of our best biscuits. 59</p>
      </div>
    </article>
    <article class="dish">
      <div class="dish-photo photo-shawarma" role="img" aria-label="Photo of chicken shawarma wraps"></div>
      <div class="dish-info">
        <h2 class="dish-name">CHICKEN SHAWARMA</h2>
        <p class="dish-desc">Served in the inimitable Quayview style with garlic sauce, cucumber and tomato pickles and three peppers coulis. 75</p>
      </div>
    </article>
    <article class="dish">
      <div class="dish-photo photo-seafood" role="img" aria-label="Photo of frutti di mare with mussels"></div>
      <div class="dish-info">
        <h2 class="dish-name">FRUTTI DI MARE</h2>
        <p class="dish-desc">Fresh cherry tomatoes, Mussels, Prawns, Calamari, Mozzarella, Olives. 99</p>
      </div>
    </article>

    <article class="dish">
      <div class="dish-photo photo-arabic" role="img" aria-label="Photo of the Arabic breakfast platter"></div>
      <div class="dish-info">
        <h2 class="dish-name">THE ARABIC BREAKFAST</h2>
        <p class="dish-desc">One choice of hot beverage from our cafe served with our selection of scones, Smoked salmon and avocado sandwich, roasted sausages sandwich, grilled vegetables sandwich, of our best biscuits. 59</p>
      </div>
    </article>
    <article class="dish">
      <div class="dish-photo photo-shawarma" role="img" aria-label="Photo of chicken shawarma wraps"></div>
      <div class="dish-info">
        <h2 class="dish-name">CHICKEN SHAWARMA</h2>
        <p class="dish-desc">Served in the inimitable Quayview style with garlic sauce, cucumber and tomato pickles and three peppers coulis. 75</p>
      </div>
    </article>
    <article class="dish">
      <div class="dish-photo photo-seafood" role="img" aria-label="Photo of frutti di mare with mussels"></div>
      <div class="dish-info">
        <h2 class="dish-name">FRUTTI DI MARE</h2>
        <p class="dish-desc">Fresh cherry tomatoes, Mussels, Prawns, Calamari, Mozzarella, Olives. 99</p>
      </div>
    </article>
  </main>
</body>
</html>
```